Business Card & Email Signature Design || Upmarket + Luxury

Riverlume Honey, a New Zealand Manuka Honey company needs a Business Card & Email Signature design.

Our logo's are attached in Gold & Black versions, feel free to be creative with how you use the logo and it's patterns in your design.

Style:
- Looking for an Elegant, Luxurious, Upmarket feel.
- Black/Matte Black Card, Gold Foil, UV Embossing

Information to Add:

- Logo
- Company Name: Riverlume Honey
- Name: Mattias Brovell
- Title: Creative Director
- Phone: +64 2919 58 617
- Email: mattias@riverlumehoney.example
- Website: www.riverlumehoney.example

- Socials: ***For email Signature Only***
- Friendloop: https://www.facebook.com/riverlumehoney/
- Snapframe: https://www.instagram.com/riverlumehoney/

Target Market(s)

Asia/Europe Luxury, Upmarket

Contact Information for Business Card

- Logo
- Name: Mattias Brovell
- Phone: +64 2919 58 617

Font styles to use
Other font styles liked:
• Champagne & Limousines (Attached)

Requirements
Must have
• Business Card & Email Signature Design.

Looking for a Sleek, Luxury, Upmarket Design.

```html
<!DOCTYPE html>
<html lang="en">
<head>
<meta charset="utf-8">
<title>Riverlume Honey – Business Card &amp; Email Signature</title>
<link href="https://fonts.googleapis.com/css2?family=Jost:wght@300;400&display=swap" rel="stylesheet">
<style>
  :root {
    --paper: #ffffff;
    --card-black: #000000;
    --sig-black: #0c0a06;
    --gold: #d8bc6e;
    --gold-light: #f1e08f;
    --gold-deep: #b8914a;
    --honey: #e8c454;
    --amber: #e0a04a;
    --rule: #2a2618;
    --ink: #111111;
  }
  * { margin: 0; padding: 0; box-sizing: border-box; }
  html, body { width: 1200px; height: 814px; overflow: hidden; background: var(--paper); }
  body { position: relative; font-family: "Jost", sans-serif; font-weight: 300; }

  .card { position: absolute; border-radius: 20px; overflow: hidden; }
  .card-front { left: 36px; top: 41px; width: 516px; height: 315px; background: var(--card-black); }
  .card-back  { left: 649px; top: 41px; width: 515px; height: 315px; background: var(--card-black); }
  .signature  { left: 203px; top: 463px; width: 783px; height: 315px;
    background: linear-gradient(112deg, var(--honey) 0%, var(--honey) 42%, var(--amber) 55%, var(--sig-black) 66%, var(--sig-black) 100%); }

  .ornament { position: absolute; left: 0; top: 0; width: 185px; height: 315px;
    background: radial-gradient(ellipse at 10% 55%, #3aa0c0 0%, #6b3f8a 14%, rgba(216,188,110,0.55) 30%, rgba(216,188,110,0.15) 65%, rgba(0,0,0,0) 100%);
    border-top-right-radius: 60% 40%; border-bottom-right-radius: 20% 60%; }

  .person-name { position: absolute; font-weight: 400; white-space: nowrap; line-height: 1; }
  .job-title { position: absolute; font-weight: 300; white-space: nowrap; line-height: 1; }

  .card-front .person-name { right: 68px; top: 34px; font-size: 42px; color: var(--gold-light); }
  .card-front .job-title { right: 73px; top: 84px; font-size: 26px; color: var(--gold-light); }

  .divider { position: absolute; height: 1px; background: var(--rule); }
  .divider-mark { position: absolute; width: 14px; height: 14px; border-radius: 50%; border: 1px solid #3a3526; }

  .contact-list { position: absolute; list-style: none; }
  .contact-list li { display: flex; align-items: center; white-space: nowrap; line-height: 1; }
  .contact-icon { width: 22px; height: 22px; flex: none; }

  .card-front .contact-list { right: 60px; top: 196px; text-align: right; }
  .card-front .contact-list li { justify-content: flex-end; gap: 18px; height: 33px; font-size: 22px; color: var(--gold); }
  .card-front .contact-list .contact-icon { stroke: #5a5440; }

  .brand { position: absolute; text-align: center; color: var(--gold); font-weight: 400; line-height: 1; white-space: nowrap; }
  .brand-dot { display: block; margin: 0 auto; border-radius: 50%; border: 2px solid var(--gold); }
  .brand-name { display: block; letter-spacing: 0.18em; }
  .brand-suffix { display: block; letter-spacing: 0.05em; }

  .card-back .brand { left: 0; width: 100%; top: 62px; }
  .card-back .brand-dot { width: 120px; height: 120px; margin-bottom: 38px; }
  .card-back .brand-name { font-size: 38px; padding-left: 0.18em; }
  .card-back .brand-suffix { font-size: 22px; margin-top: 4px; }

  .signature .person-name { left: 56px; top: 38px; font-size: 52px; }
  .signature .name-first { color: #f7eea0; }
  .signature .name-last { color: var(--ink); }
  .signature .job-title { left: 64px; top: 99px; font-size: 33px; color: var(--ink); }
  .signature .job-title .lit { color: #f7eea0; }

  .signature .contact-list { left: 46px; top: 210px; }
  .signature .contact-list li { gap: 14px; height: 27px; font-size: 21px; color: var(--ink); }
  .signature .contact-list .contact-icon { stroke: #6a5622; }

  .social-links { position: absolute; left: 393px; top: 142px; display: flex; flex-direction: column; gap: 14px; }
  .social-link { display: block; width: 40px; height: 40px; border-radius: 8px; background: var(--gold); }

  .signature .brand { left: 460px; width: 310px; top: 52px; }
  .signature .brand-dot { width: 130px; height: 130px; margin-bottom: 40px; }
  .signature .brand-name { font-size: 22px; letter-spacing: 0.12em; padding-left: 0.12em; }
  .signature .brand-suffix { font-size: 14px; margin-top: 4px; }
</style>
</head>
<body>

<section class="card card-front" aria-label="Business card front">
  <div class="ornament" role="img" aria-label="Gold filigree scroll ornament with blue, green and purple inlays along the left edge"></div>
  <h1 class="person-name">Mattias Brovell</h1>
  <p class="job-title">Creative Director</p>
  <div class="divider" style="left:235px; top:157px; width:66px;"></div>
  <div class="divider-mark" style="left:334px; top:150px;"></div>
  <div class="divider" style="left:380px; top:157px; width:66px;"></div>
  <ul class="contact-list">
    <li>+64 2919 58 617
      <svg class="contact-icon" viewBox="0 0 22 22" fill="none" stroke-width="1.2"><path d="M8 2c5 2 6 8 3 11-1 2-3 4-3 7"/></svg></li>
    <li>mattias@riverlumehoney.example
      <svg class="contact-icon" viewBox="0 0 22 22" fill="none" stroke-width="1.2"><rect x="1" y="5" width="20" height="13"/><path d="M1 5l10 8 10-8"/></svg></li>
    <li>www.riverlumehoney.example
      <svg class="contact-icon" viewBox="0 0 22 22" fill="none" stroke-width="1.2"><circle cx="11" cy="11" r="9.5"/><path d="M1.5 11h19M11 1.5c-4 5-4 14 0 19M11 1.5c4 5 4 14 0 19"/></svg></li>
  </ul>
</section>

<section class="card card-back" aria-label="Business card back">
  <div class="brand">
    <span class="brand-dot"></span>
    <span class="brand-name">RIVERLUME HONEY</span>
    <span class="brand-suffix">CO.</span>
  </div>
</section>

<section class="card signature" aria-label="Email signature">
  <h2 class="person-name"><span class="name-first">Mattias</span> <span class="name-last">Brovell</span></h2>
  <p class="job-title"><span class="lit">Creati</span>ve Director</p>
  <div class="divider" style="left:46px; top:173px; width:77px; background:#c9a640;"></div>
  <div class="divider-mark" style="left:158px; top:166px; border-color:#f7eea0;"></div>
  <div class="divider" style="left:208px; top:173px; width:77px; background:#5a4820;"></div>
  <ul class="contact-list">
    <li><svg class="contact-icon" viewBox="0 0 22 22" fill="none" stroke-width="1.2"><path d="M8 2c5 2 6 8 3 11-1 2-3 4-3 7"/></svg><span style="padding-left:14px">+64 2919 58 617</span></li>
    <li><svg class="contact-icon" viewBox="0 0 22 22" fill="none" stroke-width="1.2"><rect x="1" y="5" width="20" height="13"/><path d="M1 5l10 8 10-8"/></svg>mattias@riverlumehoney.example</li>
    <li><svg class="contact-icon" viewBox="0 0 22 22" fill="none" stroke-width="1.2"><circle cx="11" cy="11" r="9.5"/><path d="M1.5 11h19M11 1.5c-4 5-4 14 0 19M11 1.5c4 5 4 14 0 19"/></svg>www.riverlumehoney.example</li>
  </ul>
  <nav class="social-links" aria-label="Social profiles">
    <a class="social-link" href="https://snapframe.example/riverlumehoney/" aria-label="Snapframe profile"></a>
    <a class="social-link" href="https://friendloop.example/riverlumehoney/" aria-label="Friendloop profile"></a>
  </nav>
  <div class="brand">
    <span class="brand-dot"></span>
    <span class="brand-name">RIVERLUME HONEY</span>
    <span class="brand-suffix">CO.</span>
  </div>
</section>

</body>
</html>
```